Awesome new dental practice requires a New Letterhead design

We would like a new letterhead design to align with our new business branding & business cards. I have uploaded all the logos & current business card details that can be used. The new website can be viewed here https://lumaveo.com.au

Other useful details: Font Poppins
Colour Palettes:
Dark Pink #c45389
Light Pink: #e83e8c
Black

Please let me know if you have any questions or require anything else.

Industry/Entity Type

Dental

Font styles to use
Other font styles liked:
• Poppins

```html
<!DOCTYPE html>
<html lang="en">
<head>
<meta charset="utf-8">
<title>Lumaveo Letterhead</title>
<link rel="stylesheet" href="https://fonts.googleapis.com/css2?family=Poppins:ital,wght@0,400;0,500;0,600;1,600&family=Open+Sans:wght@400;600&display=swap">
<style>
  :root {
    --backdrop: #b2b2b2;
    --paper: #fafafa;
    --ink: #111111;
    --body-text: #5a5a5a;
    --brand-pink: #c9478a;
    --sign-blue: #1a7fc0;
  }
  * { margin: 0; padding: 0; box-sizing: border-box; }
  html, body { width: 1200px; height: 1001px; overflow: hidden; }
  body { background: var(--backdrop); position: relative; }
  .letterhead {
    position: absolute; left: 287px; top: 58px;
    width: 625px; height: 884px;
    background: var(--paper);
    box-shadow: 0 0 3px rgba(0,0,0,0.15);
    font-family: "Open Sans", sans-serif;
    color: var(--body-text);
  }
  .edge-band { position: absolute; left: 0; width: 17px; }
  .edge-band--dark { top: 0; height: 727px; background: var(--ink); }
  .edge-band--pink { top: 727px; height: 157px; background: var(--brand-pink); }

  .brand { position: absolute; right: 58px; top: 68px; text-align: right; font-family: "Poppins", sans-serif; }
  .brand__name { font-size: 32px; font-weight: 600; color: var(--ink); line-height: 1; letter-spacing: 0.3px; }
  .brand__descriptor { margin-top: 8px; font-size: 10px; font-weight: 600; letter-spacing: 1.6px; color: var(--ink); }

  .letter-body { position: absolute; left: 59px; width: 507px; font-size: 9.3px; line-height: 16px; }
  .salutation { top: 209px; }
  .paragraph { text-align: justify; }
  .p1 { top: 257px; } .p2 { top: 368px; } .p3 { top: 480px; }

  .signoff { position: absolute; left: 59px; top: 594px; }
  .signoff__label { font-size: 9.5px; font-weight: 600; color: #444; }
  .signoff__signature { display: block; width: 152px; height: 32px; margin-top: 8px; border-radius: 3px;
    background: linear-gradient(90deg, rgba(26,127,192,0.25), rgba(26,127,192,0.12)); }
  .signoff__role { margin-top: 10px; font-size: 9.5px; }

  .contact { position: absolute; right: 58px; top: 794px; text-align: right; font-family: "Poppins", sans-serif; color: var(--ink); font-size: 9.6px; }
  .contact__row { display: flex; justify-content: flex-end; align-items: center; gap: 12px; line-height: 16px; }
  .contact__item { display: inline-flex; align-items: center; gap: 6px; }
  .contact__item svg { width: 10px; height: 10px; fill: var(--brand-pink); }
  .contact__address { line-height: 16px; }
  .slogan { margin-top: 7px; font-size: 11.5px; font-weight: 600; font-style: italic; color: var(--brand-pink); }
  .slogan strong { color: var(--ink); font-weight: 600; }
</style>
</head>
<body>
  <main class="letterhead">
    <div class="edge-band edge-band--dark"></div>
    <div class="edge-band edge-band--pink"></div>

    <header class="brand">
      <div class="brand__name">Lumaveo</div>
      <div class="brand__descriptor">DENTISTRY &amp; ORTHODONTICS</div>
    </header>

    <p class="letter-body salutation">Dear Sir,</p>
    <p class="letter-body paragraph p1">Lorem Ipsum is simply dummy text of the printing and typesetting industry. Lorem Ipsum has been the industry's standard dummy text ever since the 1500s, when an unknown printer took a galley of type and scrambled it to make a type specimen book. It has survived not only five centuries, but also the leap into electronic typesetting, remaining essentially unchanged. It was popularised in the 1960s with the release of Letraset sheets containing Lorem Ipsum passages, and more recently with desktop publishing software like Aldus PageMaker including versions of Lorem Ipsum.</p>
    <p class="letter-body paragraph p2">Lorem Ipsum is simply dummy text of the printing and typesetting industry. Lorem Ipsum has been the industry's standard dummy text ever since the 1500s, when an unknown printer took a galley of type and scrambled it to make a type specimen book. It has survived not only five centuries, but also the leap into electronic typesetting, remaining essentially unchanged. It was popularised in the 1960s with the release of Letraset sheets containing Lorem Ipsum passages, and more recently with desktop publishing software like Aldus PageMaker including versions of Lorem Ipsum.</p>
    <p class="letter-body paragraph p3">Lorem Ipsum is simply dummy text of the printing and typesetting industry. Lorem Ipsum has been the industry's standard dummy text ever since the 1500s, when an unknown printer took a galley of type and scrambled it to make a type specimen book.</p>

    <section class="signoff">
      <p class="signoff__label">Your Name</p>
      <span class="signoff__signature" role="img" aria-label="Handwritten signature of Mark Ellison"></span>
      <p class="signoff__role">CEO &nbsp;|&nbsp; Owner</p>
    </section>

    <footer class="contact">
      <div class="contact__row">
        <span class="contact__item"><svg viewBox="0 0 10 10"><path d="M1 3.2C1 2 2.5 1 5 1s4 1 4 2.2V4H7V3.2H3V4H1zM2 4.5h6L9 8.5H1z"/></svg>(08) 9000 4127</span>
        <span class="contact__item"><svg viewBox="0 0 10 10"><path d="M0 2h10v6H0zM0.8 2.6 5 5.6 9.2 2.6"/></svg>hello@lumaveo.com.au</span>
        <span class="contact__item"><svg viewBox="0 0 10 10"><circle cx="5" cy="5" r="4.2"/></svg>www.lumaveo.com.au</span>
      </div>
      <div class="contact__address">Shop 7, 42 Marlin Street Westhaven WA 6000</div>
      <div class="slogan">Life is short. <strong>Smile</strong> while you still have teeth.</div>
    </footer>
  </main>
</body>
</html>
```